Velarine Retractable Banner

I need a banner designed to advertise my skincare brand at a meeting. I want it to be eye-catching, yet elegant and modern and it should keep with my branding from my website (www.velarine-example.com). Please let me know if you need any addition files or photos.

I have included the specs for the size I plan to order.

```html
<!DOCTYPE html>
<html lang="en">
<head>
<meta charset="utf-8">
<title>Velarine Retractable Banner</title>
<link href="https://fonts.googleapis.com/css2?family=Fraunces:opsz,wght@9..144,600;9..144,700&family=Montserrat:wght@400;500;700&display=swap" rel="stylesheet">
<style>
  :root {
    --backdrop: #3f3f3f;
    --cream-light: #fbf3e6;
    --cream: #f2e2c8;
    --cream-deep: #e6cfad;
    --copper: #a4622c;
    --brown: #7a4522;
    --brown-dark: #5b3418;
    --url-cream: #f3e2c6;
    --white: #fbfbf9;
  }
  * { margin: 0; padding: 0; box-sizing: border-box; }
  html, body { width: 1200px; height: 2575px; overflow: hidden; }
  body { background: var(--backdrop); position: relative; }
  .banner {
    position: absolute; left: 117px; top: 117px;
    width: 966px; height: 2338px; overflow: hidden;
    background: radial-gradient(ellipse at 50% 40%, var(--cream-light) 0%, var(--cream) 55%, var(--cream-deep) 100%);
  }
  .banner-art { position: absolute; left: 0; top: 0; width: 966px; height: 2338px; }
  .brand-name {
    position: absolute; left: 0; width: 100%; top: 112px; text-align: center;
    font-family: "Fraunces", Georgia, serif; font-weight: 600;
    font-size: 128px; line-height: 1; color: var(--copper); letter-spacing: -1px;
  }
  .brand-byline {
    position: absolute; left: 0; width: 100%; top: 236px; text-align: center;
    font-family: "Montserrat", Arial, sans-serif; font-weight: 500;
    font-size: 34px; color: var(--copper);
  }
  .headline {
    position: absolute; left: 0; width: 100%; top: 372px; text-align: center;
    font-family: "Fraunces", Georgia, serif; font-weight: 700;
    font-size: 112px; line-height: 120px; color: var(--brown); letter-spacing: -1px;
  }
  .tagline {
    position: absolute; font-family: "Fraunces", Georgia, serif; font-weight: 700;
    font-size: 100px; line-height: 1; color: var(--brown-dark); letter-spacing: -2px;
  }
  .tagline-love { left: 518px; top: 1488px; }
  .tagline-for  { left: 628px; top: 1570px; }
  .tagline-your { left: 586px; top: 1630px; }
  .tagline-skin { left: 628px; top: 1716px; }
  .website {
    position: absolute; left: 0; width: 100%; top: 2148px; text-align: center;
    font-family: "Montserrat", Arial, sans-serif; font-weight: 400;
    font-size: 68px; color: var(--url-cream);
  }
  .website strong { font-weight: 700; }
</style>
</head>
<body>
  <div class="banner">
    <svg class="banner-art" viewBox="0 0 966 2338" xmlns="http://www.w3.org/2000/svg">
      <defs>
        <linearGradient id="heartPhotoTone" x1="0" y1="0" x2="1" y2="1">
          <stop offset="0" stop-color="#5a4a44"/>
          <stop offset="0.45" stop-color="#d9b7a4"/>
          <stop offset="1" stop-color="#e9cdbd"/>
        </linearGradient>
        <linearGradient id="productTone" x1="0" y1="0" x2="1" y2="0">
          <stop offset="0" stop-color="#f4f4f2"/>
          <stop offset="0.5" stop-color="#ffffff"/>
          <stop offset="1" stop-color="#e3e3e0"/>
        </linearGradient>
      </defs>

      <path class="bottom-band" d="M0 1506 C 150 1630, 310 1830, 600 1940 C 750 1992, 880 2004, 966 2004 L966 2338 L0 2338 Z" fill="var(--brown-dark)" stroke="var(--copper)" stroke-width="8"/>

      <path class="heart-photo" role="img" aria-label="Photo: a woman holding a serum dropper bottle beside her eye"
        d="M484 737 C 560 660, 760 640, 880 700 C 940 740, 930 860, 860 950 C 760 1080, 560 1180, 429 1291 C 330 1160, 160 1040, 110 900 C 70 790, 120 700, 230 690 C 340 680, 420 700, 484 737 Z"
        fill="url(#heartPhotoTone)" stroke="var(--copper)" stroke-width="12" stroke-linejoin="round"/>

      <g class="accent-hearts">
        <path d="M652 1262 c-6 -14 -28 -12 -26 4 c2 12 18 20 26 28 c8 -8 24 -16 26 -28 c2 -16 -20 -18 -26 -4 Z" fill="var(--brown)"/>
        <path d="M608 1316 c-6 -14 -28 -12 -26 4 c2 12 18 20 26 28 c8 -8 24 -16 26 -28 c2 -16 -20 -18 -26 -4 Z" fill="#a86a3a"/>
        <path d="M651 1361 c-6 -14 -28 -12 -26 4 c2 12 18 20 26 28 c8 -8 24 -16 26 -28 c2 -16 -20 -18 -26 -4 Z" fill="#e3c196"/>
        <path d="M639 1423 c-6 -14 -28 -12 -26 4 c2 12 18 20 26 28 c8 -8 24 -16 26 -28 c2 -16 -20 -18 -26 -4 Z" fill="#f4e9d8"/>
      </g>

      <g class="product-lineup">
        <rect role="img" aria-label="Product photo: Soft Accord Balancing Cream pump bottle" x="89" y="1295" width="181" height="760" rx="14" fill="url(#productTone)"/>
        <path role="img" aria-label="Product photo: Soft Accord Balancing Serum dropper bottle" d="M348 1369 h60 v130 h22 q51 10 51 70 v470 q0 21 -21 21 h-164 q-21 0 -21 -21 v-470 q0 -60 51 -70 h22 Z" fill="url(#productTone)"/>
        <rect role="img" aria-label="Product photo: Weekly Tryst Exfoliator jar" x="479" y="1848" width="396" height="224" rx="22" fill="url(#productTone)"/>
      </g>
    </svg>

    <div class="brand-name">Velarine</div>
    <div class="brand-byline">by dr. elena marsh</div>
    <h1 class="headline">Get the Glow<br>of First Love</h1>

    <div class="tagline tagline-love">Love</div>
    <div class="tagline tagline-for">for</div>
    <div class="tagline tagline-your">your</div>
    <div class="tagline tagline-skin">skin</div>

    <div class="website">www.<strong>velarine-example</strong>.com</div>
  </div>
</body>
</html>
```